Flyer für Alltagsbegleitung
Zielgruppe
Firma: Tageshilfe am Fluss
Meine Zielgruppe sind alle Menschen, die im Alltag, Hilfe benötigen.
Aufgabenstellung
Der Flyer soll modern und und ansprechend aussehen. Es soll vermerkt sein, das ich als annerkannte Kraft, Entlastungsleistung nach

```html
<!DOCTYPE html>
<html lang="de">
<head>
<meta charset="utf-8">
<title>Tageshilfe am Fluss – Flyer</title>
<link href="https://fonts.googleapis.com/css2?family=Delius&family=Montserrat:wght@600;700;800&display=swap" rel="stylesheet">
<style>
  :root{
    --navy:#5a7190;
    --ink:#3c4d63;
    --ice:#d6e2ee;
    --peach:#f8c48e;
    --paper:#ffffff;
    --muted:#6f7e90;
    --photo-a:#9fb1c4;
    --photo-b:#c9b9a4;
    --photo-c:#a9c08f;
  }
  *{box-sizing:border-box;margin:0;padding:0}
  html,body{width:1200px;height:842px;overflow:hidden;background:var(--paper)}
  .flyer{position:relative;width:1200px;height:842px;font-family:"Delius",cursive;color:var(--ink)}
  .panel{position:absolute;top:0;height:842px;width:400px}
  .panel--front{left:0;background:var(--paper)}
  .panel--about{left:402px;width:398px;background:var(--ice)}
  .panel--contact{left:800px;background:var(--paper)}

  .brand{position:absolute;left:44px;top:52px;display:flex;align-items:center;gap:8px;font-size:15px;color:var(--navy)}
  .brand__dot{width:14px;height:14px;border-radius:50%;background:var(--navy)}

  .front__band{position:absolute;left:0;top:206px;width:376px;height:636px;background:var(--navy);border-top-right-radius:24px}
  .front__photo{position:absolute;left:0;top:97px;width:344px;height:427px;border-top-right-radius:24px;background:linear-gradient(135deg,var(--photo-a),var(--photo-b) 60%,#8d8a84)}
  .front__title{position:absolute;left:44px;top:566px;color:#fff}
  .front__title h1{font-family:"Montserrat",sans-serif;font-weight:800;font-size:26px;letter-spacing:.5px}
  .front__title p{font-size:20px;line-height:28px;margin-top:6px}
  .front__web{position:absolute;left:44px;top:786px;font-family:"Montserrat",sans-serif;font-weight:700;font-size:11px;color:#fff;letter-spacing:.3px}
  .front__icon{position:absolute;left:300px;top:740px}

  .quote{position:absolute;left:60px;top:92px;width:300px;font-family:"Montserrat",sans-serif;font-weight:700;font-size:17px;line-height:24px;color:var(--ink);text-transform:uppercase}
  .quote__by{position:absolute;left:80px;top:212px;font-size:12px;color:var(--muted)}
  .about__head{position:absolute;left:60px;top:282px;font-family:"Montserrat",sans-serif;font-weight:700;font-size:17px;color:var(--ink)}
  .about__text{position:absolute;left:60px;top:316px;width:310px;font-size:14px;line-height:22px;color:var(--muted)}
  .about__portrait{position:absolute;left:215px;top:525px;width:113px;height:195px;background:linear-gradient(180deg,#e9d6a6,#cdb89c 55%,#b8a690);border-radius:56px 56px 4px 4px}
  .about__button{position:absolute;left:50px;top:722px;width:282px;height:40px;border-radius:20px;background:#fff;display:flex;align-items:center;justify-content:center;font-family:"Montserrat",sans-serif;font-weight:700;font-size:11px;color:var(--ink);letter-spacing:.3px}

  .contact__photo{position:absolute;left:65px;top:0;width:335px;height:392px;border-radius:0 0 0 24px;background:linear-gradient(160deg,var(--photo-c),#d8d2c6 55%,#9aa5c4)}
  .contact__tab{position:absolute;left:65px;top:438px;width:138px;height:48px;background:var(--navy);border-radius:16px 16px 0 0;color:#fff;font-family:"Montserrat",sans-serif;font-weight:700;font-size:15px;display:flex;align-items:flex-start;justify-content:center;padding-top:12px}
  .contact__card{position:absolute;left:28px;top:484px;width:372px;height:278px;background:var(--peach);border-radius:22px 0 0 22px;padding:32px 0 0 34px}
  .contact__name,.contact__org{font-size:19px;color:var(--ink)}
  .contact__line{font-size:13px;color:var(--ink);margin-top:6px}
  .contact__caps{font-family:"Montserrat",sans-serif;font-weight:700;font-size:11px;color:var(--ink);margin-top:6px}
  .contact__org{margin-top:44px}
  .contact__icon{position:absolute;right:22px;bottom:26px}
</style>
</head>
<body>
<main class="flyer">
  <section class="panel panel--front">
    <div class="brand"><span class="brand__dot"></span>Lena Marbach</div>
    <div class="front__band"></div>
    <div class="front__photo" role="img" aria-label="Foto: Betreuerin im Gespräch mit einem älteren Herrn"></div>
    <div class="front__title">
      <h1>ALLTAGSBEGLEITUNG</h1>
      <p>Mit Herz, Verlässlichkeit<br>&amp; Erfahrung</p>
    </div>
    <div class="front__web">WWW.TAGESHILFE-FLUSS.DE</div>
    <svg class="front__icon" width="70" height="70" viewBox="0 0 70 70" fill="none" stroke="#2e3b4d" stroke-width="2" stroke-linecap="round" stroke-linejoin="round">
      <path d="M35 40 C20 30 16 20 24 14 C30 10 35 16 35 19 C35 16 40 10 46 14 C54 20 50 30 35 40Z"/>
      <path d="M6 50 C16 46 22 50 30 52 L44 52 M6 60 L40 62 C48 62 56 54 62 48"/>
    </svg>
  </section>

  <section class="panel panel--about">
    <p class="quote">„Sich um diejenigen zu kümmern, die sich einst um uns gekümmert haben, ist eine der grössten Ehren.“</p>
    <p class="quote__by">– M. Berger</p>
    <h2 class="about__head">WER BIN ICH?</h2>
    <p class="about__text">Mein Name ist Lena Marbach. Als anerkannte Betreuungskraft nach § 45b SGB XI unterstütze ich Menschen mit Pflegegrad im Alltag – flexibel, menschlich und individuell.<br>Ich biete Hilfe im Haushalt, Begleitung zu Terminen oder einfach nur ein offenes Ohr – ganz nach Ihren Bedürfnissen.</p>
    <div class="about__portrait" role="img" aria-label="Porträtfoto der Betreuerin"></div>
    <div class="about__button">ERFAHRE MEHR AUF UNSERER WEBSITE</div>
  </section>

  <section class="panel panel--contact">
    <div class="contact__photo" role="img" aria-label="Foto: Ärztin begleitet eine Seniorin mit Rollator im Freien"></div>
    <div class="contact__tab">KONTAKT</div>
    <div class="contact__card">
      <p class="contact__name">Lena Marbach</p>
      <p class="contact__line">Phone: 01520 884311</p>
      <p class="contact__caps">E-MAIL: OLUPMARBACH@POSTFACH.DE</p>
      <p class="contact__org">Tageshilfe am Fluss</p>
      <p class="contact__line">Uferweg 12, 34567 Flussstadt</p>
      <p class="contact__caps">WWW.TAGESHILFE-FLUSS.DE</p>
      <svg class="contact__icon" width="62" height="62" viewBox="0 0 62 62" fill="none" stroke="#2e3b4d" stroke-width="2" stroke-linecap="round" stroke-linejoin="round">
        <circle cx="36" cy="14" r="8"/>
        <path d="M31 26 C28 36 30 42 36 44 L48 44 M10 40 L22 34 L30 40 M8 52 L26 52 C34 52 40 48 44 44"/>
      </svg>
    </div>
  </section>
</main>
</body>
</html>
```